New business card for UK roofing company

We are Brindmore Roofing and we need a business card design for our staff.

We offer the following services:

- New roofs
- General roof repairs
- Drone surveys
- Single ply roofing
- Steel cladding
- Asbestos removal
- Electronic leak detection

I have attached our logo. I have also attached example branding printed to our vans. The business card should fit in with the style of our branding.

The business card should have the following information;

Address:
Unit 17c Wendlecroft Farm
Wendlecroft Lane
Hatchington
CM4 9QD

Telephone: 020 7946 0372
24 Hour: 0800 612 4479

Email: ray@brindmoreroofing.example
Mobile: 07700981234
Name: Ray Tunstead
Website: www.brindmoreroofing.example

The business card will be printed in Spot UV, see here: https://www.kestaprint.example/business-cards/spot-uv/

If you need anymore info, please let me know,

```html
<!DOCTYPE html>
<html lang="en">
<head>
<meta charset="utf-8">
<title>Brindmore Roofing – Business Card</title>
<link href="https://fonts.googleapis.com/css2?family=Arimo:wght@400;700&family=Roboto+Condensed:wght@700&display=swap" rel="stylesheet">
<style>
  :root {
    --navy: #0f4a7c;
    --cyan: #00aedb;
    --white: #ffffff;
    --backdrop: #ababab;
  }
  * { margin: 0; padding: 0; box-sizing: border-box; }
  html, body { width: 1200px; height: 1000px; overflow: hidden; }
  body {
    background: var(--backdrop);
    font-family: "Arimo", Arial, sans-serif;
    position: relative;
  }
  .card {
    position: absolute;
    left: 294px;
    width: 613px;
    height: 352px;
    border-radius: 28px;
    overflow: hidden;
    background: var(--white);
    box-shadow: 0 22px 40px rgba(0,0,0,0.35);
  }
  .card--front { top: 80px; }
  .card--back { top: 496px; }

  /* Front */
  .front__panel {
    position: absolute; left: 0; top: 0; width: 100%; height: 255px;
    background: var(--navy);
  }
  .front__band {
    position: absolute; left: 0; top: 255px; width: 100%; height: 18px;
    background: var(--cyan);
  }
  .front__rule {
    position: absolute; left: 0; top: 273px; width: 100%; height: 9px;
    background: var(--navy);
  }
  .brand {
    position: absolute; display: flex; align-items: center;
    font-weight: 700; white-space: nowrap;
  }
  .brand__dot { border-radius: 50%; background: var(--cyan); flex: none; }
  .front__brand { left: 58px; top: 38px; gap: 14px; }
  .front__brand .brand__dot { width: 64px; height: 64px; }
  .front__brand .brand__name { color: var(--white); font-size: 50px; letter-spacing: -1.5px; }
  .front__tagline {
    position: absolute; left: 149px; top: 106px;
    color: var(--white); font-size: 22px; font-weight: 700; letter-spacing: 0.5px;
  }
  .front__phone {
    position: absolute; left: 149px; top: 156px;
    display: flex; align-items: center; gap: 6px;
    color: var(--cyan);
    font-family: "Roboto Condensed", "Arial Narrow", sans-serif;
    font-size: 46px; font-weight: 700; line-height: 1;
  }
  .front__phone svg { width: 28px; height: 28px; }
  .front__hotline {
    position: absolute; left: 149px; top: 204px;
    color: var(--white); font-size: 27px; line-height: 1;
  }
  .front__hotline strong { font-weight: 700; }
  .services {
    position: absolute; left: 0; top: 294px; width: 100%;
    text-align: center; color: var(--navy);
    font-size: 16.5px; font-weight: 700; line-height: 21px; letter-spacing: 0.35px;
  }

  /* Back */
  .back__art { position: absolute; left: 0; top: 0; }
  .contact {
    position: absolute; left: 43px; top: 38px;
    color: var(--white); font-size: 14.5px; line-height: 19px;
  }
  .contact__name { font-size: 16.5px; font-weight: 700; margin-bottom: 10px; }
  .contact__group { margin-bottom: 18px; }
  .contact__web { font-weight: 700; font-size: 14px; }
  .back__brand { left: 40px; top: 290px; gap: 6px; }
  .back__brand .brand__dot { width: 26px; height: 26px; }
  .back__brand .brand__name { color: var(--navy); font-size: 24px; letter-spacing: -0.8px; }
  .back__tagline {
    position: absolute; left: 70px; top: 321px;
    color: var(--navy); font-size: 11px; font-weight: 700;
  }
</style>
</head>
<body>

<section class="card card--front">
  <div class="front__panel"></div>
  <div class="front__band"></div>
  <div class="front__rule"></div>

  <div class="brand front__brand">
    <span class="brand__dot"></span>
    <span class="brand__name">brindmoreroofing</span>
  </div>
  <p class="front__tagline">Your local roofing experts</p>
  <p class="front__phone">
    <svg viewBox="0 0 24 24" aria-hidden="true"><path fill="currentColor" d="M6.6 10.8c1.4 2.8 3.8 5.1 6.6 6.6l2.2-2.2c.3-.3.7-.4 1-.2 1.1.4 2.3.6 3.6.6.6 0 1 .4 1 1V20c0 .6-.4 1-1 1C10.6 21 3 13.4 3 4c0-.6.4-1 1-1h3.5c.6 0 1 .4 1 1 0 1.3.2 2.5.6 3.6.1.3 0 .7-.2 1L6.6 10.8z"/></svg>
    020 7946 0372
  </p>
  <p class="front__hotline"><strong>24 Hour:</strong> 0800 612 4479</p>

  <p class="services">
    New roofs | General roof repairs | Drone surveys| Single ply roofing<br>
    Steel cladding | Asbestos removal | Electronic leak detection
  </p>
</section>

<section class="card card--back">
  <svg class="back__art" width="613" height="352" viewBox="0 0 613 352" aria-hidden="true">
    <polygon points="0,0 613,0 613,236 0,258" fill="var(--navy)"/>
    <polygon points="0,260 613,238 613,250 0,272" fill="var(--cyan)"/>
    <polygon points="0,273 613,251 613,255 0,277" fill="var(--navy)"/>
    <circle cx="500" cy="200" r="200" fill="var(--cyan)" stroke="var(--white)" stroke-width="8"/>
  </svg>

  <div class="contact">
    <p class="contact__name">Ray Tunstead</p>
    <p class="contact__group">ray@brindmoreroofing.example<br>07700981234</p>
    <p class="contact__group">Unit 17c Wendlecroft Farm,<br>Wendlecroft Lane, Hatchington,<br>Chelmsford CM4 9QD</p>
    <p class="contact__web">www.brindmoreroofing.example</p>
  </div>

  <div class="brand back__brand">
    <span class="brand__dot"></span>
    <span class="brand__name">brindmoreroofing</span>
  </div>
  <p class="back__tagline">Your local roofing experts</p>
</section>

</body>
</html>
```